Food Packaging Design Project

We already have an established brand but feel that our packaging could be stronger. We would like the same logo outline , colour scheme and wording on the front and back... so that it is still recognisable to our customers but just a little more professional looking with the wow factor to help it stand out on the shelve.

We need both front and back design with colours on the back also.

The design must contain our registered logo design but can be added to.

The back doesn't have to be split into 2 columns as in the image provided.

The packets arn't the same as the old packs (as in picture attached) but instead will be pouches with solid edges.

We will need working files so that we can amend ourselves once the final design has been chosen.

Thanks in advance!

Reason: havent quite got what we are after, not enough designs submitted.

• The design must contain our registered logo... see image attached.

Must contain our colour that we currently have.

Must have the same writing on the front and back.

```html
<!DOCTYPE html>
<html lang="en">
<head>
<meta charset="utf-8">
<title>Slim Strands – Original pack front</title>
<link rel="stylesheet" href="https://fonts.googleapis.com/css2?family=Bubblegum+Sans&family=Comic+Neue:wght@700&display=swap">
<style>
  :root {
    --brand-red: #a81e27;
    --banner-red: #c0363d;
    --tan: #f3d190;
    --leaf-green: #9aa654;
    --leaf-light: #9db05a;
    --leaf-dark: #6c7c30;
    --paper: #ffffff;
    --ink-red: #a51c24;
  }
  * { box-sizing: border-box; margin: 0; padding: 0; }
  html, body { width: 952px; height: 1200px; overflow: hidden; background: var(--paper); }
  .pack {
    position: relative;
    width: 952px;
    height: 1200px;
    overflow: hidden;
    background: var(--paper);
    font-family: "Bubblegum Sans", cursive;
  }
  .pack__backdrop { position: absolute; inset: 0; }
  .claims-corner {
    position: absolute;
    left: 0; top: 44px;
    width: 298px; height: 152px;
    background: var(--brand-red);
    border-radius: 0 22px 22px 0;
    color: var(--paper);
    font-size: 47px;
    line-height: 1.05;
    padding: 14px 0 0 44px;
  }
  .tag-pill {
    position: absolute;
    left: 638px; width: 289px;
    background: var(--tan);
    border-radius: 30px;
    color: var(--ink-red);
    font-size: 38px;
    letter-spacing: 1px;
    line-height: 0.95;
    padding-left: 38px;
  }
  .tag-pill--calories { top: 40px; height: 88px; padding-top: 6px; }
  .tag-pill--organic { top: 139px; height: 60px; display: flex; align-items: center; }
  .brand-banner {
    position: absolute;
    left: 152px; top: 622px;
    width: 712px; height: 206px;
    background: var(--banner-red);
    border-radius: 16px;
    text-align: center;
  }
  .brand-banner__name {
    font-family: "Comic Neue", sans-serif;
    font-weight: 700;
    font-size: 96px;
    color: var(--paper);
    line-height: 1;
    padding-top: 18px;
  }
  .brand-banner__tagline {
    position: absolute;
    left: 40px; right: 40px; bottom: 24px;
    height: 54px;
    background: var(--paper);
    border-radius: 27px;
    color: var(--ink-red);
    font-size: 33px;
    display: flex; align-items: center; justify-content: center;
  }
  .flavour-pill {
    position: absolute;
    left: 521px; top: 889px;
    width: 358px; height: 62px;
    background: var(--paper);
    border: 4px solid var(--leaf-dark);
    border-radius: 31px;
    color: var(--ink-red);
    font-size: 42px;
    letter-spacing: 1px;
    display: flex; align-items: center; justify-content: center;
  }
  .zero-badges { position: absolute; left: 0; top: 1011px; width: 952px; height: 136px; }
  .zero-badge {
    position: absolute;
    top: 0;
    width: 136px; height: 136px;
    border-radius: 50%;
    background: var(--paper);
    display: flex; align-items: center; justify-content: center;
  }
  .zero-badge__label {
    width: 134px; height: 58px;
    background: var(--brand-red);
    border-radius: 6px;
    color: var(--paper);
    font-size: 25px;
    line-height: 1;
    text-align: center;
    display: flex; flex-direction: column; justify-content: center;
  }
</style>
</head>
<body>
<main class="pack">
  <svg class="pack__backdrop" width="952" height="1200" viewBox="0 0 952 1200" aria-hidden="true">
    <defs>
      <linearGradient id="circleShade" x1="0" y1="0" x2="1" y2="1">
        <stop offset="0" stop-color="var(--leaf-light)"/>
        <stop offset="1" stop-color="var(--leaf-dark)"/>
      </linearGradient>
    </defs>
    <rect width="952" height="1200" fill="var(--leaf-green)"/>
    <path d="M0 0 H952 V715 C880 900 660 975 480 975 C250 975 60 850 0 640 Z" fill="var(--paper)"/>
    <path d="M0 0 H303 L0 298 Z" fill="var(--brand-red)"/>
    <circle cx="463" cy="463" r="309" fill="url(#circleShade)"/>
  </svg>

  <div class="claims-corner">Fat Free<br>Wheat Free</div>

  <div class="tag-pill tag-pill--calories">8 Calories<br>PerPack</div>
  <div class="tag-pill tag-pill--organic">Organic</div>

  <div class="brand-banner">
    <h1 class="brand-banner__name">Slim Strands</h1>
    <p class="brand-banner__tagline">The Alternative To Pasta For Weight Loss</p>
  </div>

  <div class="flavour-pill">Original</div>

  <div class="zero-badges">
    <div class="zero-badge" style="left:95px"><div class="zero-badge__label"><span>Zero</span><span>Net Cals</span></div></div>
    <div class="zero-badge" style="left:307px"><div class="zero-badge__label"><span>Zero</span><span>Sugar</span></div></div>
    <div class="zero-badge" style="left:514px"><div class="zero-badge__label"><span>Zero</span><span>Salt</span></div></div>
    <div class="zero-badge" style="left:722px"><div class="zero-badge__label"><span>Zero</span><span>Gluten</span></div></div>
  </div>
</main>
</body>
</html>
```